Website for our 3rd party logistics warehouse company

Our company is a 3rd party logistics company. We receive and ship other businesses products for them. We offer our services to other smaller businesses that do not have a warehouse to operate out of. We also help many Brindlemart businesses prepare their products to be sold on Brindlemart.

We are looking for a modern looking design for our website. Please see our attached logo for design ideas. We are open to changing logo colors for website.

We really like the look of the website www.quorvela.com

Target Market(s)

Other businesses and brands of products

Industry/Entity Type

Warehousing and shipping

Number of Pages Required

2 page

Requirements
Must have
• We need 2 pages. Our main landing page and a duplicate page with different information geared towards brands.
Nice to have
• I like the look of overlay/transparent sections. Please see quorvela.com there is a ribbon that shows "Partners".

```html
<!DOCTYPE html>
<html lang="en">
<head>
<meta charset="utf-8">
<title>Keystride 3PL – Warehousing &amp; Fulfillment</title>
<link href="https://fonts.googleapis.com/css2?family=Playfair+Display:wght@700;800&family=Rubik:wght@300;400;500;700&display=swap" rel="stylesheet">
<style>
:root{
  --yellow:#ffc83d;
  --yellow-deep:#f5b800;
  --ink:#1b1b1b;
  --night:#14171d;
  --night-2:#23272f;
  --grey-text:#6d6d6d;
  --soft:#f7f7f7;
  --line:#e6e6e6;
  --white:#ffffff;
}
*{box-sizing:border-box;margin:0;padding:0}
html,body{width:1200px;height:4000px;overflow:hidden}
body{position:relative;font-family:"Rubik",sans-serif;color:var(--ink);background:var(--white);font-weight:300}
.abs{position:absolute}
.serif{font-family:"Playfair Display",serif;font-weight:800}
.brand{font-family:"Rubik",sans-serif;font-weight:500;letter-spacing:2px;color:var(--white);font-size:19px;display:flex;align-items:center;gap:10px}
.brand .dot{width:14px;height:14px;border-radius:50%;background:var(--yellow)}
.btn{display:flex;align-items:center;justify-content:center;background:var(--yellow);border-radius:30px;font-weight:500;font-size:12px;text-transform:uppercase;color:var(--ink)}

/* top bar */
.topbar{left:0;top:0;width:1200px;height:44px;background:var(--yellow);font-size:13px;font-weight:400}
.topbar .mail{left:162px;top:14px;display:flex;gap:10px;align-items:center}
.topbar .logins{right:178px;top:14px;display:flex;gap:14px;align-items:center}
.topbar .sep{width:1px;height:14px;background:rgba(0,0,0,.3)}

/* hero */
.hero{left:0;top:44px;width:1200px;height:571px;background:linear-gradient(180deg,#3a3c3f 0%,#2a2e33 40%,#3e3b34 75%,#1e2228 100%)}
.hero .shade{left:0;top:0;width:1200px;height:571px;background:linear-gradient(180deg,rgba(0,0,0,.35),rgba(0,0,0,.15) 60%,rgba(0,0,0,.4))}
.hero .logo{left:158px;top:54px}
.nav{left:482px;top:54px;display:flex;gap:18px;font-size:12px;font-weight:500;color:var(--white)}
.phone-btn{left:875px;top:36px;width:167px;height:42px;font-size:14px;gap:8px;text-transform:none}
.hero-kicker{left:0;width:1200px;top:208px;text-align:center;color:var(--yellow);font-size:15px;font-weight:400}
.hero-title{left:0;width:1200px;top:240px;text-align:center;color:var(--white);font-size:43px;font-weight:700}
.hero-text{left:300px;width:600px;top:310px;text-align:center;color:#e8e8e8;font-size:12.5px;line-height:24px;font-weight:300}
.hero-cta{left:514px;top:380px;width:171px;height:44px}
.dots{left:1074px;top:280px;display:flex;flex-direction:column;gap:26px}
.dots span{width:6px;height:6px;border-radius:50%;background:var(--white)}
.dots span.on{background:var(--yellow);box-shadow:0 0 0 4px rgba(255,200,61,.3)}

/* partners */
.partners{left:0;top:615px;width:1200px;height:78px;border-bottom:1px solid var(--line);display:flex;justify-content:space-between;align-items:center;padding:0 160px}
.partner{display:flex;align-items:center;gap:9px;color:#a5a5a5;font-size:17px;font-weight:400;letter-spacing:1.5px}
.partner i{width:22px;height:22px;border:2px solid #bdbdbd;display:block}

/* who we are */
.section-title{left:0;width:1200px;text-align:center;font-size:23px;letter-spacing:.5px}
.who-text{left:340px;width:520px;top:768px;text-align:center;font-size:12.5px;line-height:24px;color:var(--grey-text)}
.service{width:300px;text-align:center}
.service .pic{width:230px;height:230px;border-radius:50%;margin:0 auto}
.service h3{font-family:"Playfair Display",serif;font-weight:700;font-size:17px;margin-top:16px}
.service p{font-size:12.5px;line-height:24px;color:var(--grey-text);margin-top:8px;padding:0 10px}

/* why */
.why{left:0;top:1257px;width:1200px;height:463px;background:linear-gradient(180deg,#151a24 0%,#1d222c 50%,#2a2a2a 100%)}
.why-card{top:1412px;width:203px;height:224px;background:var(--white);text-align:center;padding-top:26px}
.why-card p{font-size:12.5px;line-height:22px;color:#555;margin-top:18px;padding:0 12px}
.why-card svg.wave{position:absolute;left:0;bottom:8px}

/* benefits */
.benefits{left:0;top:1720px;width:1200px;height:527px;background:var(--soft);overflow:hidden}
.benefit-text{font-size:12.5px;line-height:24px;color:#555}
.ring-icon{width:90px;height:90px;border-radius:50%;background:var(--yellow);display:flex;align-items:center;justify-content:center}

/* software */
.software-title{left:158px;top:2380px;font-size:23px;letter-spacing:1px}
.software-text{left:158px;top:2432px;width:330px;font-size:12.5px;line-height:24px;color:#555}
.more-btn{left:155px;top:2553px;width:135px;height:40px;font-size:11px}

/* guarantee */
.guarantee{left:0;top:2755px;width:1200px;height:427px;background:linear-gradient(100deg,#3b342b 0%,#2b2824 45%,#1a1c21 60%,#22252b 100%)}
.g-title{left:710px;top:2820px;color:var(--white);font-size:23px;letter-spacing:.5px}
.g-label{color:var(--white);font-size:12.5px;font-weight:400}
.g-text{left:712px;top:2998px;width:330px;color:#f0f0f0;font-size:12.5px;line-height:24px}

/* form */
.field{height:57px;border:1px solid var(--line);display:flex;align-items:center;justify-content:space-between;padding:0 22px;font-size:12.5px;color:#777}
.send-btn{left:517px;top:3567px;width:172px;height:50px;font-size:11px;gap:8px}

/* footer */
.footer{left:0;top:3655px;width:1200px;height:345px;background:#111214}
.f-head{top:3719px;color:var(--white);font-weight:500;font-size:14px}
.f-line{color:#d8d8d8;font-size:12.5px;line-height:30px}
.fine{left:155px;top:3868px;width:890px;color:#666;font-size:8.5px;line-height:14px}
.copy{left:0;width:1200px;top:3954px;text-align:center;color:#666;font-size:9px}
.f-rule{left:0;top:3850px;width:1200px;height:1px;background:#222}
</style>
</head>
<body>

<!-- top bar -->
<div class="abs topbar">
  <div class="abs mail">
    <svg width="16" height="12" viewBox="0 0 16 12"><rect x="1" y="1" width="14" height="10" fill="none" stroke="#1b1b1b" stroke-width="1.3"/><path d="M1 1l7 6 7-6" fill="none" stroke="#1b1b1b" stroke-width="1.3"/></svg>
    sales@keystride3pl.com
  </div>
  <div class="abs logins">
    <svg width="13" height="14" viewBox="0 0 13 14"><circle cx="6.5" cy="4" r="3" fill="none" stroke="#1b1b1b" stroke-width="1.2"/><path d="M1 13c0-3 2.5-5 5.5-5s5.5 2 5.5 5" fill="none" stroke="#1b1b1b" stroke-width="1.2"/></svg>
    <span>Client Login</span><span class="sep"></span><span>Vendor Login</span>
  </div>
</div>

<!-- hero -->
<section class="abs hero" role="img" aria-label="Aerial photo of a container port at dusk">
  <div class="abs shade"></div>
  <div class="abs logo brand"><span class="dot"></span>KEYSTRIDE 3PL</div>
  <nav class="abs nav"><span>HOME</span><span>GROW</span><span>DISTRIBUTE</span><span>ABOUT US</span><span>CONTACT US</span></nav>
  <div class="abs btn phone-btn">
    <svg width="15" height="15" viewBox="0 0 24 24"><path d="M6.6 10.8c1.4 2.8 3.8 5.1 6.6 6.6l2.2-2.2c.3-.3.7-.4 1-.2 1.1.4 2.3.6 3.6.6.6 0 1 .4 1 1V20c0 .6-.4 1-1 1C10.6 21 3 13.4 3 4c0-.6.4-1 1-1h3.5c.6 0 1 .4 1 1 0 1.3.2 2.5.6 3.6.1.3 0 .7-.2 1z" fill="none" stroke="#1b1b1b" stroke-width="2"/></svg>
    <b style="font-weight:500">(123) 555 01 48</b>
  </div>
  <div class="abs hero-kicker">TRANSPORT YOUR GOODS</div>
  <h1 class="abs hero-title serif" style="font-weight:700">Locally And Around The World</h1>
  <p class="abs hero-text">Denounce with righteous indignation and dislike men who are beguiled and demoralized by the charms of pleasure of the moment so blinded by desire, that they cannot foresee the pain and trouble.</p>
  <div class="abs btn hero-cta">CONTACT US NOW</div>
  <div class="abs dots"><span></span><span class="on"></span><span></span></div>
</section>

<!-- partners -->
<div class="abs partners">
  <div class="partner"><i></i>MINDFORGE</div>
  <div class="partner"><i></i>HALVERN</div>
  <div class="partner"><i style="border-radius:50%"></i>TESSARO</div>
  <div class="partner"><i></i>KINETRA</div>
  <div class="partner"><i></i>LEDGERLY</div>
</div>

<!-- who we are -->
<h2 class="abs section-title serif" style="top:722px">WHO WE ARE</h2>
<p class="abs who-text">Keystride 3PL is your one stop 3PL that will help you grow your business and allow you to be hands off. We offer high end services and meet our commitment, guaranteed.</p>
<svg class="abs" style="left:0;top:950px" width="1200" height="110" viewBox="0 0 1200 110">
  <path d="M0 60 C60 -10 120 0 185 60" fill="none" stroke="#cfcfcf" stroke-dasharray="5 5"/>
  <path d="M412 30 C440 10 470 20 490 40" fill="none" stroke="#cfcfcf" stroke-dasharray="5 5"/>
  <path d="M712 30 C740 10 770 20 790 40" fill="none" stroke="#cfcfcf" stroke-dasharray="5 5"/>
  <path d="M1015 40 C1060 -10 1100 20 1130 80 C1150 110 1180 90 1200 60" fill="none" stroke="#cfcfcf" stroke-dasharray="5 5"/>
</svg>
<div class="abs service" style="left:147px;top:860px">
  <div class="pic" role="img" aria-label="Warehouse interior with stacked pallets" style="background:linear-gradient(180deg,#d8d8d6,#8e8a80 55%,#5a4a38)"></div>
  <h3>Warehousing</h3>
  <p>We automate and manage inventory through multiple channels in facilities nationwide</p>
</div>
<div class="abs service" style="left:453px;top:860px">
  <div class="pic" role="img" aria-label="Cargo truck, containers and airplane at sunset" style="background:linear-gradient(180deg,#6f95c6,#e9a45a 55%,#3c3f4a)"></div>
  <h3>Transportation</h3>
  <p>We are a licensed transportation logistics broker providing local and regional ground transportation and drayage services</p>
</div>
<div class="abs service" style="left:753px;top:860px">
  <div class="pic" role="img" aria-label="Workers moving cardboard boxes" style="background:linear-gradient(160deg,#7d8286,#4a5056 55%,#a48a6a)"></div>
  <h3>Fulfillment</h3>
  <p>We use the best technology &amp; workflows to provide the most efficient fulfillment solutions</p>
</div>

<!-- why -->
<section class="abs why" role="img" aria-label="Dark photo of a port at night"></section>
<h2 class="abs section-title serif" style="top:1326px;color:#fff">WHY USE A KEYSTRIDE 3PL?</h2>
<div class="abs why-card" style="left:155px">
  <svg width="60" height="60" viewBox="0 0 60 60"><circle cx="28" cy="30" r="22" fill="none" stroke="#1b1b1b" stroke-width="2"/><path d="M6 30h44M28 8c-8 8-8 36 0 44M28 8c8 8 8 36 0 44" fill="none" stroke="#1b1b1b" stroke-width="1.5"/><path d="M44 22c-5 0-8 4-8 8 0 5 8 13 8 13s8-8 8-13c0-4-3-8-8-8z" fill="#ffc83d" stroke="#1b1b1b" stroke-width="1.5"/><circle cx="44" cy="30" r="2.5" fill="#1b1b1b"/></svg>
  <p>Work from anywhere<br>in the world.</p>
  <svg class="wave" width="203" height="20" viewBox="0 0 203 20"><path d="M0 12 C50 0 100 20 150 8 C175 2 190 8 203 10" fill="none" stroke="#ffc83d" stroke-width="1.5"/></svg>
</div>
<div class="abs why-card" style="left:384px">
  <svg width="60" height="60" viewBox="0 0 60 60"><circle cx="30" cy="36" r="9" fill="none" stroke="#1b1b1b" stroke-width="2"/><path d="M14 58c0-9 7-13 16-13s16 4 16 13" fill="none" stroke="#1b1b1b" stroke-width="2"/><ellipse cx="24" cy="12" rx="14" ry="8" fill="#ffc83d" stroke="#1b1b1b" stroke-width="1.5"/><ellipse cx="40" cy="14" rx="10" ry="7" fill="#fff" stroke="#1b1b1b" stroke-width="1.5"/></svg>
  <p>Don't have to manage employees, health insurance plans, payroll, sick calls, etc.</p>
  <svg class="wave" width="203" height="20" viewBox="0 0 203 20"><path d="M0 12 C50 0 100 20 150 8 C175 2 190 8 203 10" fill="none" stroke="#ffc83d" stroke-width="1.5"/></svg>
</div>
<div class="abs why-card" style="left:611px">
  <svg width="60" height="60" viewBox="0 0 60 60"><path d="M4 24L30 6l26 18v32H4z" fill="none" stroke="#1b1b1b" stroke-width="2"/><rect x="16" y="30" width="28" height="26" fill="none" stroke="#1b1b1b" stroke-width="2"/><rect x="24" y="38" width="12" height="10" fill="#ffc83d" stroke="#1b1b1b" stroke-width="1.5"/><path d="M16 36h28" stroke="#1b1b1b" stroke-width="1.5"/></svg>
  <p>Don't get locked into a 3-5 year warehouse lease where you guarantee hundreds of thousands of dollars</p>
  <svg class="wave" width="203" height="20" viewBox="0 0 203 20"><path d="M0 12 C50 0 100 20 150 8 C175 2 190 8 203 10" fill="none" stroke="#ffc83d" stroke-width="1.5"/></svg>
</div>
<div class="abs why-card" style="left:840px">
  <svg width="60" height="60" viewBox="0 0 60 60"><rect x="14" y="30" width="32" height="26" rx="3" fill="none" stroke="#1b1b1b" stroke-width="2"/><path d="M24 50V40l6-6v6h8v10z" fill="#ffc83d" stroke="#1b1b1b" stroke-width="1.5"/><path d="M30 24V6M24 12l6-6 6 6M18 24V14M14 18l4-4 4 4M42 24V14M38 18l4-4 4 4" fill="none" stroke="#1b1b1b" stroke-width="1.8"/></svg>
  <p>Grow your business<br>without commitment</p>
  <svg class="wave" width="203" height="20" viewBox="0 0 203 20"><path d="M0 12 C50 0 100 20 150 8 C175 2 190 8 203 10" fill="none" stroke="#ffc83d" stroke-width="1.5"/></svg>
</div>

<!-- benefits -->
<section class="abs benefits">
  <svg class="abs" style="left:0;top:0" width="1200" height="527" viewBox="0 0 1200 527">
    <defs><linearGradient id="hub" x1="0" y1="0" x2="0" y2="1"><stop offset="0" stop-color="#3a3a3c"/><stop offset="1" stop-color="#141518"/></linearGradient></defs>
    <circle cx="600" cy="470" r="280" fill="var(--yellow)"/>
    <circle cx="600" cy="470" r="262" fill="url(#hub)"/>
  </svg>
  <div class="abs brand" style="left:460px;top:370px;font-size:32px;letter-spacing:4px"><span class="dot" style="width:20px;height:20px"></span>KEYSTRIDE 3PL</div>
</section>
<h2 class="abs section-title serif" style="top:1765px">KEYSTRIDE 3PL BENEFITS</h2>
<div class="abs benefit-text" style="left:500px;width:200px;top:1832px;text-align:center">No receiving fees</div>

<div class="abs ring-icon" style="left:555px;top:1866px">
  <svg width="50" height="50" viewBox="0 0 50 50"><circle cx="25" cy="25" r="21" fill="none" stroke="#1b1b1b" stroke-width="2"/><rect x="8" y="19" width="34" height="12" fill="#ffc83d" stroke="#1b1b1b" stroke-width="1.5"/><text x="25" y="29" text-anchor="middle" font-family="Rubik,sans-serif" font-weight="700" font-size="9" fill="#1b1b1b">NO FEE</text></svg>
</div>
<div class="abs ring-icon" style="left:367px;top:1940px">
  <svg width="50" height="50" viewBox="0 0 50 50"><rect x="6" y="14" width="30" height="22" fill="none" stroke="#1b1b1b" stroke-width="2"/><path d="M10 22h14M10 28h10" stroke="#1b1b1b" stroke-width="2"/><path d="M34 34l4-20 6 4-4 18z" fill="none" stroke="#1b1b1b" stroke-width="2"/></svg>
</div>
<div class="abs ring-icon" style="left:761px;top:1940px">
  <svg width="50" height="50" viewBox="0 0 50 50"><rect x="6" y="24" width="38" height="18" fill="none" stroke="#1b1b1b" stroke-width="2"/><circle cx="25" cy="33" r="5" fill="none" stroke="#1b1b1b" stroke-width="2"/><path d="M20 22c-4-6 0-14 5-14s9 8 5 14" fill="none" stroke="#1b1b1b" stroke-width="2"/></svg>
</div>
<div class="abs ring-icon" style="left:292px;top:2087px">
  <svg width="56" height="56" viewBox="0 0 56 56"><circle cx="28" cy="28" r="22" fill="none" stroke="#1b1b1b" stroke-width="2" stroke-dasharray="3 3"/><text x="28" y="30" text-anchor="middle" font-family="Rubik,sans-serif" font-weight="700" font-size="13" fill="#1b1b1b">48</text><text x="28" y="39" text-anchor="middle" font-family="Rubik,sans-serif" font-weight="500" font-size="6" fill="#1b1b1b">HOURS</text></svg>
</div>
<div class="abs ring-icon" style="left:817px;top:2087px">
  <svg width="50" height="50" viewBox="0 0 50 50"><rect x="14" y="6" width="22" height="38" rx="3" fill="none" stroke="#1b1b1b" stroke-width="2"/><rect x="8" y="16" width="20" height="14" fill="#ffc83d" stroke="#1b1b1b" stroke-width="1.5"/><path d="M8 16l10 8 10-8" fill="none" stroke="#1b1b1b" stroke-width="1.5"/></svg>
</div>
<div class="abs benefit-text" style="left:185px;width:160px;top:1955px;text-align:right">No monthly subscription – only pay for what you use</div>
<div class="abs benefit-text" style="left:870px;width:200px;top:1966px">No pallet or outbound fees</div>
<div class="abs benefit-text" style="left:140px;width:136px;top:2093px;text-align:right">48 hour turn around guarantee done in 48 hours or its free*</div>
<div class="abs benefit-text" style="left:925px;width:120px;top:2107px">Email and phone support</div>

<!-- software -->
<h2 class="abs software-title serif">OUR SOFTWARE</h2>
<p class="abs software-text">Know what inventory is at our warehouse in real time. Our software allows you to track your inventory and know how your shipment status in real time. Professional software designed specifically for our needs.</p>
<div class="abs btn more-btn">MORE DETAILS</div>
<svg class="abs" style="left:530px;top:2290px" width="560" height="420" viewBox="0 0 560 420">
  <circle cx="405" cy="70" r="68" fill="none" stroke="#ffc83d" stroke-width="2"/>
  <circle cx="315" cy="390" r="28" fill="none" stroke="#ffc83d" stroke-width="2"/>
</svg>
<div class="abs" role="img" aria-label="Inventory dashboard shown on laptop, tablet and phone" style="left:540px;top:2342px;width:535px;height:335px;background:linear-gradient(135deg,#2c2c2e 0%,#e9ecef 18%,#f4f5f7 55%,#d9d9dc 85%,#2c2c2e 100%);border-radius:10px"></div>

<!-- guarantee -->
<section class="abs guarantee" role="img" aria-label="Warehouse floor with stacked cartons"></section>
<h2 class="abs g-title serif">OUR GUARANTEE</h2>
<svg class="abs" style="left:708px;top:2880px" width="80" height="56" viewBox="0 0 80 56"><path d="M2 18h16M6 28h12M2 38h16" stroke="#ffc83d" stroke-width="3"/><circle cx="48" cy="28" r="24" fill="#ffc83d"/><text x="48" y="37" text-anchor="middle" font-family="Rubik,sans-serif" font-weight="700" font-size="24" fill="#1b1b1b">48</text></svg>
<svg class="abs" style="left:835px;top:2876px" width="64" height="60" viewBox="0 0 64 60"><circle cx="38" cy="18" r="14" fill="#ffc83d"/><text x="38" y="24" text-anchor="middle" font-family="Rubik,sans-serif" font-weight="700" font-size="16" fill="#1b1b1b">%</text><path d="M4 42h14l10 4h18l12-10 2 4-14 16H20L4 54z" fill="#ffc83d"/></svg>
<div class="abs g-label" style="left:712px;top:2952px">Business Hours</div>
<div class="abs g-label" style="left:837px;top:2952px">We offer a 500 item (up to $700)</div>
<p class="abs g-text">All orders will be prepped and ready for shipment in 48 business hours (often 24 or less) and we guarantee it. We are confident in our services and if we do not fulfill our obligation, we offer a 500 item (up to $700) credit on your next shipment.</p>

<!-- contact form -->
<form class="abs" style="left:231px;top:3283px;width:746px">
  <div class="abs field" style="left:0;top:0;width:356px">Full Name
    <svg width="18" height="20" viewBox="0 0 18 20"><circle cx="9" cy="6" r="4" fill="none" stroke="#bbb"/><rect x="2" y="12" width="14" height="7" fill="none" stroke="#bbb"/></svg></div>
  <div class="abs field" style="left:390px;top:0;width:356px">Email Address
    <svg width="18" height="14" viewBox="0 0 18 14"><rect x="1" y="1" width="16" height="12" fill="none" stroke="#bbb"/><path d="M1 1l8 6 8-6" fill="none" stroke="#bbb"/></svg></div>
  <div class="abs field" style="left:0;top:82px;width:356px">Company Name
    <svg width="18" height="20" viewBox="0 0 18 20"><rect x="3" y="2" width="12" height="17" fill="none" stroke="#bbb"/><path d="M6 6h2M10 6h2M6 10h2M10 10h2M6 14h2M10 14h2" stroke="#bbb"/></svg></div>
  <div class="abs field" style="left:390px;top:82px;width:356px">Your Topic
    <svg width="18" height="20" viewBox="0 0 18 20"><rect x="2" y="2" width="14" height="17" fill="none" stroke="#bbb"/><path d="M5 7h8M5 11h8M5 15h5" stroke="#bbb"/></svg></div>
  <div class="abs field" style="left:0;top:157px;width:746px;height:100px;align-items:flex-start;justify-content:flex-start;gap:14px;padding-top:24px">Message
    <svg width="26" height="16" viewBox="0 0 26 16"><rect x="1" y="1" width="16" height="11" fill="none" stroke="#bbb"/><rect x="8" y="5" width="16" height="10" fill="#fff" stroke="#bbb"/></svg></div>
</form>
<div class="abs btn send-btn">SEND MESSAGE
  <svg width="12" height="12" viewBox="0 0 12 12"><path d="M2 10L10 2M4 2h6v6" fill="none" stroke="#1b1b1b" stroke-width="1.4"/></svg></div>

<!-- footer -->
<footer class="abs footer"></footer>
<div class="abs brand" style="left:165px;top:3738px;font-size:16px"><span class="dot"></span>KEYSTRIDE 3PL</div>
<div class="abs f-head" style="left:387px">Contact us</div>
<div class="abs f-line" style="left:387px;top:3752px">help@keystride3pl.com<br>+(123)555-014-2290</div>
<div class="abs f-head" style="left:612px">Visit us</div>
<div class="abs f-line" style="left:612px;top:3752px">482 Larchmont Way,<br>Carver, IL 62900</div>
<div class="abs f-head" style="left:840px">Follow us</div>
<div class="abs" style="left:842px;top:3762px;display:flex;gap:14px">
  <span style="width:12px;height:12px;border-radius:50%;background:#cfcfcf;display:block"></span>
  <span style="width:12px;height:12px;border-radius:50%;background:#cfcfcf;display:block"></span>
  <span style="width:12px;height:12px;border-radius:50%;background:#cfcfcf;display:block"></span>
</div>
<div class="abs f-rule"></div>
<p class="abs fine">*Our guarantee is 48 hours from the time an outbound shipment is created in our system. Weekends and holidays excluded. Orders created on a Friday after hours, Saturday or Sunday count from opening on Monday. We offer a credit of up to 500 units on your next shipment. Outbound shipments leave after daily pickup.</p>
<div class="abs copy">© 2021 KEYSTRIDE 3PL.com. All Rights Reserved</div>

</body>
</html>
```